Email Newsletter template for organization (Mailchimp)

We need a newsletter-editable-template designed for Mailchimp that reflects our style preferences as reflected in our website (lanternfieldtrust.org) and should include the following elements:

- Large images that are as wide as or wider than the text beneath.

- A single column with 4-5 similarly structured items.

- Clean, text-free social media links at the top and bottom of the newsletter (with a slightly different look) along with social media share buttons (no text) associated with each of our story items.

Our organization is called the Lanternfield Trust for Uplift, and we work to remove barriers to opportunity in the areas of education, employment, and family formation. I've attached our effort at putting together what we have in mind but we are not entirely happy with it.

The name of the newsletter is "Wayposts" and we have a tag line that says "A digest exploring the intersection of public policy and civil society."

We would like our current logo (attached) *creatively edited* to include the title of the newsletter (but not the tag line).

The design has to be platform and browser-friendly. Coding and implementation is included in this project. The winner will provide the codes and implement it in our MailChimp account.

You can take a look here for an idea of designs we've used for publications:

http://lanternfieldtrust.org/resources/

Target Market(s)

Individuals, families and organizations concerned about the plight of the poor, feel somewhat frustrated by the lack of change in society, and are looking for ways to reach the poor and want to learn more about the groups that are doing that work.

Industry/Entity Type

Non-Profit

Coding

Coded - Design and coding required

Font styles to use
Other font styles liked:
• We like the legibility of arial but are not tied to it.

Requirements
Must have
• It has to be designed for Mailchimp and editable. It must reflect our organizations look and feel (see our website). It must be compatible with the major platforms and browsers. It must be awesome! :)
Nice to have
• Clean design with large images, limited text, easy social media engagement across items.
Should not have
• We do not want areas for a lot of text. No animation. No flash.

```html
<!DOCTYPE html>
<html lang="en">
<head>
<meta charset="utf-8">
<title>Wayposts — Lanternfield Trust for Uplift</title>
<link rel="stylesheet" href="https://fonts.googleapis.com/css2?family=Open+Sans:wght@400;600;700&family=Source+Sans+3:wght@400;600;700&display=swap">
<style>
:root{
  --navy:#0e4674;
  --navy-dark:#0b3a60;
  --page:#d1d6db;
  --white:#ffffff;
  --panel:#efefef;
  --gold:#b48a27;
  --gold-btn:#a9851f;
  --red:#b3202b;
  --text:#3c3c3c;
  --muted:#8a8a8a;
}
*{box-sizing:border-box;margin:0;padding:0}
html,body{width:1200px;height:3644px;overflow:hidden}
body{background:var(--page);font-family:"Open Sans",Arial,sans-serif;color:var(--text);position:relative}
.top-band{position:absolute;left:0;top:0;width:1200px;height:155px;background:var(--navy)}
.newsletter{position:relative;width:812px;margin:0 auto}
.utility-bar{height:49px;display:flex;align-items:center;justify-content:space-between;color:var(--white);font-size:13px;font-weight:700}
.view-link{display:flex;align-items:center;gap:8px;text-decoration:underline;letter-spacing:.3px}
.share-group{display:flex;gap:14px}
.share-btn{display:flex;align-items:center;border:2px solid var(--white);height:32px;font-size:13px;letter-spacing:.5px}
.share-btn span{padding:0 12px}
.share-btn i{width:30px;height:28px;border-left:2px solid var(--white);display:flex;align-items:center;justify-content:center}
.share-btn i b{width:12px;height:12px;background:var(--white);display:block}
.masthead{height:104px;background:var(--white);display:flex;align-items:center;justify-content:space-between;padding:0 14px 0 20px}
.brand{display:flex;align-items:center;gap:12px;font-family:"Source Sans 3",Arial,sans-serif;font-weight:700;font-size:26px;color:var(--navy)}
.brand-mark{width:30px;height:30px;background:var(--navy)}
.masthead-phone{display:flex;align-items:center;gap:10px;font-family:"Source Sans 3",Arial,sans-serif;font-weight:700;font-size:27px;color:#8a8a8a}
.hero{position:relative;height:406px;background:linear-gradient(180deg,#6f97c9 0%,#9cb7d6 30%,#8a7b62 55%,#5b5a50 78%,#3d5a35 100%)}
.hero-label{position:absolute;left:0;top:226px;height:41px;width:175px;background:var(--gold);color:var(--white);font-family:"Source Sans 3",Arial,sans-serif;font-weight:700;font-size:24px;display:flex;align-items:center;padding-left:18px;letter-spacing:.5px}
.hero-tagline{position:absolute;left:0;top:275px;width:328px;height:131px;background:var(--red);color:var(--white);font-family:"Source Sans 3",Arial,sans-serif;font-weight:700;font-size:24px;line-height:31px;padding:14px 18px;text-transform:uppercase}
.story{text-align:center;padding:30px 17px 0}
.story.light{background:var(--white)}
.story.tinted{background:var(--panel)}
.story-title{font-family:"Source Sans 3",Arial,sans-serif;font-weight:600;font-size:27px;line-height:34px;color:var(--gold);text-transform:uppercase;padding:0 40px}
.story-date{font-size:14px;color:var(--muted);margin-top:4px}
.story-image{width:778px;height:381px;margin-top:18px}
.story-text{font-size:17px;line-height:26px;padding:16px 36px 0}
.btn{display:inline-block;margin-top:20px;height:42px;line-height:42px;padding:0 0;width:228px;color:var(--white);font-size:14px;font-weight:700;border-radius:3px;text-transform:uppercase;letter-spacing:.2px}
.btn.gold{background:var(--gold-btn)}
.btn.navy{background:var(--navy)}
.site-footer{background:var(--white);height:224px;padding:34px 17px 0}
.footer-url{font-family:"Source Sans 3",Arial,sans-serif;font-size:29px;font-weight:600;color:var(--gold)}
.footer-row{display:flex;justify-content:space-between;align-items:flex-end;margin-top:28px}
.footer-contact{font-size:14px;line-height:22px}
.footer-contact .line{display:flex;gap:28px}
.footer-contact .line span{display:flex;align-items:center;gap:8px}
.footer-contact a{color:var(--gold);text-decoration:underline}
.social{display:flex;gap:12px;margin-bottom:6px}
.social i{width:46px;height:46px;display:block}
.social .s1{background:#1f4f8f}
.social .s2{background:#27a3d9}
.social .s3{background:#d8242a}
.social .s4{background:#d9473a}
</style>
</head>
<body>
<div class="top-band"></div>
<main class="newsletter">
  <div class="utility-bar">
    <span class="view-link">
      <svg width="14" height="12" viewBox="0 0 14 12"><rect x="1" y="1" width="12" height="8" fill="none" stroke="#fff" stroke-width="1.6"/><rect x="4" y="10" width="6" height="1.6" fill="#fff"/></svg>
      VIEW THIS MAIL IN YOUR BROWSER
    </span>
    <div class="share-group">
      <span class="share-btn"><span>POST</span><i><b></b></i></span>
      <span class="share-btn"><span>SHARE</span><i><b></b></i></span>
    </div>
  </div>

  <header class="masthead">
    <div class="brand"><span class="brand-mark"></span>Lanternfield Trust for Uplift</div>
    <div class="masthead-phone">
      <svg width="26" height="22" viewBox="0 0 26 22"><path d="M2 8c0-4 5-6 11-6s11 2 11 6l-5 2-2-4H9L7 10z" fill="#8a8a8a"/><rect x="5" y="11" width="16" height="10" rx="2" fill="#8a8a8a"/></svg>
      CALL : 404-555-0187
    </div>
  </header>

  <section class="hero" role="img" aria-label="City skyline with a domed state capitol building under a blue sky">
    <div class="hero-label">WAYPOSTS</div>
    <div class="hero-tagline">A digest exploring the inter&shy;section of public policy and civil society</div>
  </section>

  <article class="story light" style="height:709px">
    <h2 class="story-title">White Paper: An Alternative to Incarceration – Parental Accountability Courts in Georgia</h2>
    <p class="story-date">Published in July 2015</p>
    <div class="story-image" role="img" aria-label="Judge's gavel resting on a wooden desk" style="background:linear-gradient(160deg,#2a2420 0%,#4a3628 45%,#7a5535 75%,#3a2a20 100%)"></div>
    <p class="story-text">This white paper highlights the success that Parental Accountability Courts (PACs) have had in helping chronic non-payers of child support overcome barriers to employment and pay child support regularly.</p>
    <a class="btn gold">Download White Paper</a>
  </article>

  <article class="story tinted" style="height:719px">
    <h2 class="story-title">Report: Fortifying Pathways</h2>
    <p class="story-date">Published in December 2014</p>
    <div class="story-image" role="img" aria-label="Smiling student holding a folder in a bright campus hallway" style="background:linear-gradient(120deg,#c7d3c9 0%,#e9ece6 40%,#d9c9bc 60%,#aab7b0 100%)"></div>
    <p class="story-text">this report serves as an overview of the themes and key issues covered by LTU's College and Career Pathways working group. It discusses the importance for Georgia to move away from big policy as a means of education reform.</p>
    <a class="btn navy">Download Report</a>
  </article>

  <article class="story light" style="height:661px">
    <h2 class="story-title">Report: A High Price to Pay</h2>
    <div class="story-image" role="img" aria-label="Hand stacking rows of coins on a white table" style="background:linear-gradient(180deg,#2e2e30 0%,#8d8d8f 35%,#e6e6e6 60%,#f4f4f4 100%);margin-top:14px"></div>
    <p class="story-text">this report provides solutions that aim to minimize the role debt has in driving recidivism rates. People often leave prison owing tens of thousands of dollars in debt, creating serious obstacles to a successful reentry.</p>
    <a class="btn gold">View Details</a>
  </article>

  <article class="story tinted" style="height:748px">
    <h2 class="story-title">Report: Increasing Employment Opportunities<br>for Ex-Offenders</h2>
    <p class="story-date">Published in December 2013</p>
    <div class="story-image" role="img" aria-label="Construction worker in a hard hat working under wooden roof beams" style="background:linear-gradient(135deg,#c89a68 0%,#a8744a 40%,#6a4a32 70%,#3a8a8a 100%)"></div>
    <p class="story-text">this report focuses on ways to improve workforce reentry for ex-offenders in Georgia. LTU offers six recommendations for Georgia to consider implementing and is a product of LTU's Prisoner Reentry Working Group that is developing solutions for curbing recidivism.</p>
    <a class="btn navy">Download Report</a>
  </article>

  <footer class="site-footer">
    <div class="footer-url">www.lanternfieldtrust.org</div>
    <div class="footer-row">
      <div class="footer-contact">
        <div class="line">
          <span><svg width="14" height="10" viewBox="0 0 14 10"><rect width="14" height="10" fill="#b48a27"/><path d="M0 0l7 5 7-5" fill="none" stroke="#fff" stroke-width="1.2"/></svg>info@lanternfieldtrust.org</span>
          <span><svg width="14" height="12" viewBox="0 0 26 22"><path d="M2 8c0-4 5-6 11-6s11 2 11 6l-5 2-2-4H9L7 10z" fill="#b48a27"/><rect x="5" y="11" width="16" height="10" rx="2" fill="#b48a27"/></svg>404-555-0187</span>
        </div>
        <div>© 2016 Lanternfield Trust for Uplift All rights reserved.</div>
        <div>Not Interested In Our Newsletter? <a>unsubscribe.</a></div>
      </div>
      <div class="social" aria-label="Social links">
        <i class="s1"></i><i class="s2"></i><i class="s3"></i><i class="s4"></i>
      </div>
    </div>
  </footer>
</main>
</body>
</html>
```